A unique communication angle to crowdfunding

Looking for a fresh redesign of a crowd funding website that deals in real estate. I already have the content, but am looking to take the design to the next level.

Existing real estate crowd funding sites focus on the real estate. I want to explore communication angle that:
- puts the investor in the centre of the communication: "become a baron"
- highlights the international nature (international properties, international investors)

There's also quite a lot of copy on the site, as we need to explain the service in quite a bit of detail. There's room to reduce the copy and replace with graphics. Could also consider clicking to see different text (see our difference section in http://galatownfeed.com)

The backend of the platform is already being worked on by a specialist crowd funding service provider.

In total there are 5 pages to be designed.

The homepage is really important. Right now it looks quite dated. It doesn't have a great layout. Note there is no mobile version of the website, so the pages need to be seen well on mobile devices. When looking at the brief, refer to the following links too:

current website:
http://pooltenant.com

some revisions made so far:
http://preview.fundmerrow.com/2G5GO2

Attached are logo files and another file which contained copy for the pages. No need to rework the logo.

Please make sure to use the same copy in the brief on the webpages, to ensure the layouts work. Designers are free to propose images they feel work on the pages.

I would like to see if rather than tweaking the pages, it's possible to come up with a better design concept. If the 5 pages are accepted, there's a chance I'll request an additional 4 pages.
Updates

Please note the font used in the logo is called "harabara" in case you decide to use it in any of the titles, etc.

Please note there is one additional page for which we would like to review designs. Note the page would be a template to be used on all future real estate detail pages. Here is an example of the current design for reference:

http://pooltenant.com/projects/view/14

In total there are 5 page designs required, (homepage + 4)

Thank you

FYI -

Just a quick note to give information from similar UK real estate crowdfunding sites:
http://www.estatewren.co.uk
http://plotharbor.co.uk
https://www.tilgarcap.com

Of the above, only plotharbor has a nice clean looking landing page. Information is clear and well laid out.

Hi all, just uploaded a new file in the brief. Contains some comments and a website reference. I thought it may help to explain how we could convey international aspect as well as how we could convey images in a more modern way. This is an option you can consider, but its entirely up to you how how answer the brief. Thanks!

We would like to let you know that we have just shortlisted the best designs. Together with that, we have also passed some detailed feedback to all designers who weren't shortlisted. If we didn't contact you, please let us know. If you haven't submitted a design or are working on revisions, please note these will no longer be taken into account now. We hope you understand that we need to close the project today. Thank you all once again for your great work and design concepts. Here's hoping we meet again on a future design brief. Cheers, pooltenant team.

Target Market(s)

At the moment, only rich are able to buy real estate. With this service, anyone can become a landlord. Target buyers:

Young professionals, looking to diversify from stock market and lower risk
People nearing retirement, looking for stable rental incomes
Retirees - looking to supplement pensions with possibility of capital gains
Parents - looking for a way to save long term for their children (instead of low interest paying bank accounts)

Industry/Entity Type

Communication

Font styles to use
Sans Serif
Other font styles liked:
• harabara

Colors
add136
f5f9eb
959595
000000

Requirements
Must have
• Overall, the site must convey "whoever you are, you too can become a landlord", and that you don't need to be wealthy to invest in real estate. See

Communication should put the investor (or the baron) at the centre. The investor can be any of those described in the target market.

Show the aspirational side of property ownership.

In addition to the investor/baron character, the second main theme is international. No other real estate crowdfunding website highlights this.
Nice to have
• Banner could show different consumer types, to illustrate that the service can appeal to many different profiles. Refer to attached file "home page reference - plainasdew.com" as an example of how this could be done.

Aim to show the international side of the service. Properties around the world, investors around the world.

```html
<!DOCTYPE html>
<html lang="en">
<head>
<meta charset="utf-8">
<title>Pool Tenant – International Community</title>
<link rel="stylesheet" href="https://fonts.googleapis.com/css2?family=Ubuntu:wght@500;700&family=Questrial&display=swap">
<style>
  :root {
    --green-title: #7cc242;
    --green-card: #6bbf1b;
    --green-card-edge: #54a010;
    --frame-dark: #2f3235;
    --ink: #3a3a3a;
    --grey-text: #6f6f6f;
    --grey-logo: #5e5e5e;
    --grey-icon: #8a8a8a;
    --rule: #5a7a92;
    --page: #ffffff;
  }
  * { box-sizing: border-box; margin: 0; padding: 0; }
  html, body { width: 1200px; height: 1116px; overflow: hidden; background: var(--page); }
  body { position: relative; font-family: "Questrial", sans-serif; color: var(--ink); }

  .section-title {
    position: absolute; left: 0; width: 1200px; text-align: center;
    font-family: "Ubuntu", sans-serif; font-weight: 500; color: var(--green-title);
    font-size: 31px; line-height: 38px; letter-spacing: 0; text-transform: uppercase;
  }
  .intro-title { top: 34px; }
  .intro-text {
    position: absolute; top: 84px; left: 0; width: 1200px; text-align: center;
    font-size: 16.5px; line-height: 21px; color: var(--ink);
  }

  .feature-card {
    position: absolute; top: 170px; width: 306px; height: 231px;
    background: var(--green-card); border: 1px solid var(--green-card-edge);
  }
  .feature-card:nth-of-type(1) { left: 110px; }
  .feature-card:nth-of-type(2) { left: 446px; }
  .feature-card:nth-of-type(3) { left: 782px; }
  .feature-photo {
    position: absolute; left: 9px; top: 10px; width: 286px; height: 146px;
    border: 4px solid var(--frame-dark);
  }
  .photo-network { background: radial-gradient(circle at 50% 55%, #dfe9f1 0%, #9db8cf 55%, #6f8ea9 100%); }
  .photo-growth { background: linear-gradient(180deg, #e9eef1 0%, #b9c3ca 55%, #7f8a92 100%); }
  .feature-caption {
    position: absolute; left: 0; top: 166px; width: 100%; text-align: center;
    font-family: "Ubuntu", sans-serif; font-weight: 500; color: #fff;
    font-size: 17px; line-height: 19px; text-transform: uppercase;
  }

  .featured-title { top: 443px; }

  .press-strip {
    position: absolute; left: 133px; top: 518px; width: 933px; height: 122px; background: #fff;
    box-shadow: 0 -8px 10px -8px rgba(0,0,0,0.45), 0 8px 10px -8px rgba(0,0,0,0.55);
  }
  .press-list {
    position: absolute; left: 0; top: 0; width: 100%; height: 100%;
    display: flex; align-items: center; justify-content: space-around; padding: 0 16px;
    list-style: none;
  }
  .press-name {
    font-family: "Questrial", sans-serif; color: var(--grey-logo);
    font-size: 16px; letter-spacing: 0.3px; white-space: nowrap;
  }
  .carousel-arrow {
    position: absolute; top: 565px; width: 23px; height: 29px;
    background: #f4f4f4; border: 1px solid #cfcfcf; border-radius: 3px;
  }
  .carousel-arrow.prev { left: 110px; }
  .carousel-arrow.next { left: 1066px; }
  .carousel-arrow svg { display: block; margin: 8px auto 0; }

  .follow-label { position: absolute; left: 118px; top: 678px; font-size: 14px; color: var(--ink); }
  .social-list { position: absolute; left: 118px; top: 716px; display: flex; gap: 7px; list-style: none; }
  .social-dot { width: 33px; height: 33px; border-radius: 50%; display: block; }
  .social-dot.dark { background: #5b5b5b; }
  .social-dot.light { background: var(--grey-icon); opacity: .75; }
  .group-note {
    position: absolute; left: 298px; top: 680px; width: 540px; text-align: center;
    font-size: 14px; line-height: 18.5px; color: var(--ink);
  }
  .group-name {
    position: absolute; left: 868px; top: 674px; width: 170px; text-align: right;
    font-family: "Questrial", sans-serif; font-size: 34px; line-height: 34px; color: #222;
  }

  .footer-rule { position: absolute; left: 110px; top: 766px; }
  .copyright {
    position: absolute; top: 790px; left: 0; width: 1200px; text-align: center;
    font-size: 14px; color: var(--ink);
  }
  .legal {
    position: absolute; left: 110px; width: 954px; text-align: center;
    font-size: 13px; line-height: 18.3px; color: var(--grey-text);
  }
  .legal.first { top: 841px; }
  .legal.second { top: 953px; }
  .bottom-rule { position: absolute; left: 115px; top: 1090px; }
</style>
</head>
<body>
  <header>
    <h1 class="section-title intro-title">Be part of a growing international community</h1>
    <p class="intro-text">Gain access to new projects in world class cities and join our growing community of<br>international landlords.</p>
  </header>

  <section class="features">
    <article class="feature-card">
      <div class="feature-photo photo-network" role="img" aria-label="Globe surrounded by a network of investor profile portraits"></div>
      <h2 class="feature-caption">A community of international<br>property barons</h2>
    </article>
    <article class="feature-card">
      <div class="feature-photo photo-network" role="img" aria-label="Globe linked to investors around the world"></div>
      <h2 class="feature-caption">Collective buying power of<br>the pooltenant community</h2>
    </article>
    <article class="feature-card">
      <div class="feature-photo photo-growth" role="img" aria-label="Business people before a city skyline with rising growth arrows"></div>
      <h2 class="feature-caption">Attractive real estate from<br>around the world</h2>
    </article>
  </section>

  <section class="press">
    <h2 class="section-title featured-title">Featured in</h2>
    <div class="press-strip">
      <ul class="press-list">
        <li class="press-name">Ledgerline</li>
        <li class="press-name">Tech Harbour</li>
        <li class="press-name">crowdwire.org</li>
        <li class="press-name">Crowd Forum</li>
        <li class="press-name">LaunchHK</li>
        <li class="press-name">Brassfield Weekly</li>
        <li class="press-name">Daily Tide</li>
      </ul>
    </div>
    <span class="carousel-arrow prev" aria-label="Previous"><svg width="8" height="12" viewBox="0 0 8 12"><path d="M6.5 1 L1.5 6 L6.5 11" fill="none" stroke="#777" stroke-width="2"/></svg></span>
    <span class="carousel-arrow next" aria-label="Next"><svg width="8" height="12" viewBox="0 0 8 12"><path d="M1.5 1 L6.5 6 L1.5 11" fill="none" stroke="#777" stroke-width="2"/></svg></span>
  </section>

  <footer>
    <p class="follow-label">Follow Pool Tenant On</p>
    <ul class="social-list">
      <li><span class="social-dot dark" aria-label="Social profile one"></span></li>
      <li><span class="social-dot light" aria-label="Social profile two"></span></li>
    </ul>
    <p class="group-note">Pool Tenant is part of the Kelvar Group. The Kelvar Group is a worldwide pioneer and leader in the crowd investing, peer to peer and online investment market.</p>
    <p class="group-name">kelvar<br>group</p>

    <svg class="footer-rule" width="940" height="16" viewBox="0 0 940 16" aria-hidden="true">
      <line x1="8" y1="8" x2="932" y2="8" stroke="var(--rule)" stroke-width="1.5"/>
      <path d="M0 8 L8 0 L16 8 L8 16 Z" fill="var(--rule)"/>
      <path d="M924 8 L932 0 L940 8 L932 16 Z" fill="var(--rule)"/>
    </svg>
    <p class="copyright">© pooltenant 2014</p>

    <p class="legal first">By accessing this site and any pages thereof, you agree to be bound by the terms and conditions. This website is only suitable, intended and available for professional or sophisticated, or similar investors in other jurisdictions, or those who are members of pooltenant community and familiar with, and willing to, accept the risks associated with private participation. Pooltenant does not endorse any of the projects that appear on this website, nor does it make any recommendations regarding the appropriateness of particular opportunities for any participant. Each potential participant must review and evaluate the projects in his or her own discretion and determine the suitability of participating.</p>
    <p class="legal second">This website (the "Site") is in every respect unaffiliated with any site to which it links or to any company or entity (and connected projects, investment opportunity or similar) featured on this Site, and is not meant as an endorsement of any of those companies or entities ("third parties"). Furthermore and for the avoidance of doubt, Pooltenant Limited is in no way affiliated with any third parties featured or referenced on this Site. There is no commercial relationship between Pooltenant Limited and such third parties, nor an agency arrangement or similar. If you believe your Content (including third party content) as each such term is defined in our Terms of Service has been reproduced on the Site without permission, please refer to our Terms of Service for information on how to request its removal from the Site.</p>

    <svg class="bottom-rule" width="930" height="16" viewBox="0 0 930 16" aria-hidden="true">
      <rect x="0" y="1" width="930" height="4" fill="var(--rule)"/>
      <path d="M459 5 L467 13 L475 5 Z" fill="var(--rule)"/>
    </svg>
  </footer>
</body>
</html>
```